Business Consultant need 4 page Eye Popping infographic type brochure

I am a business growth coach who operates in the visual communications industry.
I need for A4 size visuals that are clean looking, compelling and communicate clearly. The purpose is to visually explain how our new service works.
I’m looking for a clean style where the visuals pop off the page. Lots of white space.
The finished files must be ready by Monday, 13 February
If you are submitting sample work, you can do just one of the pages from those numbered 2 - 4.
I have provided hand drawn specs in the attached PDF - QNT5 Value Framework Hand Drawn Specs.
I have provided you with 10 different infographic samples that I like in this folder - Infographic Samples
I have also attached our general branding guidelines with the typical colour palette we work from in this PDF - Branding Guidelines
I need a supporting visual/logo for the name of each of the 4 services. We have a logo image for the 60-Day Climb (waiting on the final file) and I have provided samples for the other 3 in this folder - Logo Samples. You need to create the 3 missing logos.
We have a number of additional similar projects over the coming weeks and that means I’m looking for a great designer that I can form a long term relationship.
Looking forward to seeing your work
Reason: Working on the files
Target Market(s)
See attached branding guidelines
Industry/Entity Type
Business
Other font styles liked:
- See attached branding guidelines
Requirements
Must have
- See samples & branding guidelines
Nice to have
Should not have

```html
<!DOCTYPE html>
<html lang="en">
<head>
<meta charset="utf-8">
<title>QNT5 Value Framework – Service Overview</title>
<link href="https://fonts.googleapis.com/css2?family=Roboto:wght@400;500;700&display=swap" rel="stylesheet">
<style>
:root{
  --purple:#3a2c86;
  --red:#c8202f;
  --orange:#f26b21;
  --green:#1f9a3c;
  --magenta:#d81b60;
  --yellow:#f7a823;
  --ink:#2e2e2e;
  --charcoal:#3c3c3c;
  --pillar:#dcdce6;
  --gap:#e9e9ec;
  --stage:#efefef;
}
*{margin:0;padding:0;box-sizing:border-box}
html,body{width:1200px;height:1200px;overflow:hidden}
body{background:var(--stage);font-family:"Roboto",Arial,sans-serif;position:relative}
.page{position:absolute;width:496px;height:352px;background:#fff}
.page svg{display:block;width:496px;height:352px}
.page--overview{left:88px;top:208px}
.page--profit{left:616px;top:208px}
.page--climb{left:88px;top:640px}
.page--lean{left:616px;top:640px}
text{font-family:"Roboto",Arial,sans-serif}
.t-title{font-size:21px;font-weight:400}
.t-band{font-size:10.5px;fill:#fff}
.t-small{font-size:6.5px;fill:var(--ink)}
.t-tiny{font-size:5.5px;fill:var(--ink)}
.t-white{fill:#fff}
.t-bold{font-weight:700}
.mid{text-anchor:middle}
.icon-line{fill:none;stroke:#fff;stroke-width:2.4;stroke-linecap:round;stroke-linejoin:round}
.icon-fill{fill:#fff}
</style>
</head>
<body>

<!-- Overview page -->
<section class="page page--overview">
<svg viewBox="0 0 496 352" aria-label="The Business Growth Acceleration System">
  <polygon class="roof" points="12,110 248,14 484,110 478,114 248,26 18,114" fill="var(--purple)"/>
  <text class="brand-name mid" x="248" y="86" font-size="28" font-weight="700" fill="var(--ink)">QNT5</text>
  <rect class="system-banner" x="44" y="108" width="408" height="22" fill="var(--purple)"/>
  <text class="t-band mid" x="248" y="123">The Business Growth Acceleration System</text>

  <g class="pillar">
    <rect x="74" y="130" width="52" height="8" rx="3" fill="var(--red)"/>
    <rect x="80" y="136" width="40" height="98" fill="var(--pillar)"/>
    <text class="mid" transform="translate(104 185) rotate(-90)" font-size="11" fill="#444">Profit Mapping</text>
    <rect x="69" y="234" width="62" height="31" fill="var(--red)" role="img" aria-label="Rising chart icon"/>
  </g>
  <g class="pillar">
    <rect x="222" y="130" width="52" height="8" rx="3" fill="var(--orange)"/>
    <rect x="228" y="136" width="40" height="98" fill="var(--pillar)"/>
    <text class="mid" transform="translate(252 185) rotate(-90)" font-size="11" fill="#444">60-Day Climb</text>
    <rect x="217" y="234" width="62" height="31" fill="var(--orange)" role="img" aria-label="60-Day Climb emblem"/>
  </g>
  <g class="pillar">
    <rect x="370" y="130" width="52" height="8" rx="3" fill="var(--green)"/>
    <rect x="376" y="136" width="40" height="98" fill="var(--pillar)"/>
    <text class="mid" transform="translate(400 185) rotate(-90)" font-size="11" fill="#444">Lean Leadership</text>
    <rect x="365" y="234" width="62" height="31" fill="var(--green)" role="img" aria-label="Lean Leadership emblem"/>
  </g>

  <rect class="plinth" x="30" y="265" width="436" height="7" fill="var(--charcoal)"/>
  <rect class="process-band" x="10" y="272" width="476" height="36" fill="var(--purple)"/>
  <g class="process-steps t-white" font-size="6.8" text-anchor="middle" fill="#fff">
    <text x="58" y="288">Clarity Of</text><text x="58" y="296">Outcome</text>
    <text x="153" y="288">Measure</text><text x="153" y="296">What Matters</text>
    <text x="248" y="284">Execute On</text><text x="248" y="292">What</text><text x="248" y="300">Matters Most</text>
    <text x="343" y="284">Create</text><text x="343" y="292">Accountability</text><text x="343" y="300">For Key Results</text>
    <text x="438" y="288">Review Learn</text><text x="438" y="296">Adapt Grow</text>
  </g>
  <g class="process-arrows" fill="#fff">
    <polygon points="106,282 114,290 106,298"/>
    <polygon points="202,282 210,290 202,298"/>
    <polygon points="298,282 306,290 298,298"/>
    <polygon points="394,282 402,290 394,298"/>
  </g>
  <rect class="promise" x="0" y="308" width="496" height="44" fill="var(--charcoal)"/>
  <text class="mid" x="248" y="325" font-size="8" fill="#fff">The £1% Promise: Add 1% Of Total Sales To Your Bottom Line Guaranteed</text>
  <text class="mid" x="248" y="338" font-size="8" fill="#fff">Example:  £10m In Annual Sales / £100k To Bottom Line / £500k Over 5 Years</text>
</svg>
</section>

<!-- Profit Mapping page -->
<section class="page page--profit">
<svg viewBox="0 0 496 352" aria-label="Profit Mapping">
  <defs>
    <linearGradient id="trendTint" x1="0" x2="1" y1="0" y2="0">
      <stop offset="0" stop-color="#f26b21" stop-opacity="0.08"/>
      <stop offset="0.5" stop-color="#f26b21" stop-opacity="0.25"/>
      <stop offset="1" stop-color="#f26b21" stop-opacity="0.08"/>
    </linearGradient>
  </defs>
  <rect x="0" y="0" width="496" height="352" fill="var(--gap)"/>
  <rect x="0" y="0" width="496" height="142" fill="#fff"/>
  <rect x="0" y="154" width="496" height="98" fill="#fff"/>
  <rect x="0" y="264" width="496" height="88" fill="#fff"/>

  <text class="t-title" x="20" y="23" fill="var(--red)">PROFIT <tspan fill="var(--purple)">MAPPING</tspan></text>
  <rect class="trend-area" x="220" y="4" width="250" height="20" fill="url(#trendTint)" role="img" aria-label="Decorative rising trend line"/>
  <rect x="0" y="27" width="496" height="18" fill="var(--purple)"/>
  <text class="t-band mid" x="248" y="40">Create Continuous Improvement That Delivers Improved Financial Performance</text>

  <g class="system-card">
    <rect x="10" y="58" width="64" height="74" rx="4" fill="#fff" stroke="var(--red)" stroke-width="0.8"/>
    <circle cx="42" cy="80" r="14" fill="var(--red)" role="img" aria-label="Presentation board icon"/>
    <text class="t-tiny mid" x="42" y="109">The <tspan fill="var(--red)">6 Step</tspan></text>
    <text class="t-tiny mid" x="42" y="116">Profit Mapping</text>
    <text class="t-tiny mid" x="42" y="123">System</text>
  </g>
  <g class="focus-ring">
    <circle cx="130" cy="95" r="34" fill="#fff" stroke="var(--purple)" stroke-width="7"/>
    <text class="t-tiny mid t-bold" x="130" y="91">Manufacturing</text>
    <text class="t-tiny mid t-bold" x="130" y="98">Office</text>
    <text class="t-tiny mid t-bold" x="130" y="105">Technology / IT</text>
    <text class="mid" x="130" y="64" font-size="4.5" fill="#fff">More</text>
    <text class="mid" x="130" y="130" font-size="4.5" fill="#fff">Faster</text>
  </g>
  <g class="six-steps">
    <line x1="180" y1="82" x2="486" y2="82" stroke="var(--purple)" stroke-width="1.2"/>
    <polygon points="486,79 492,82 486,85" fill="var(--purple)"/>
    <g fill="var(--purple)" stroke="#fff" stroke-width="1.5">
      <circle cx="203" cy="82" r="9"/><circle cx="255" cy="82" r="9"/><circle cx="307" cy="82" r="9"/>
      <circle cx="359" cy="82" r="9"/><circle cx="411" cy="82" r="9"/><circle cx="462" cy="82" r="9"/>
    </g>
    <g font-size="10" fill="#fff" text-anchor="middle">
      <text x="203" y="86">1</text><text x="255" y="86">2</text><text x="307" y="86">3</text>
      <text x="359" y="86">4</text><text x="411" y="86">5</text><text x="462" y="86">6</text>
    </g>
    <g fill="var(--orange)">
      <rect x="180" y="104" width="46" height="14"/><rect x="232" y="104" width="46" height="14"/>
      <rect x="284" y="104" width="46" height="14"/><rect x="336" y="104" width="46" height="14"/>
      <rect x="388" y="104" width="46" height="14"/><rect x="439" y="104" width="46" height="14"/>
    </g>
    <g font-size="6.5" fill="#fff" text-anchor="middle">
      <text x="203" y="113.5">Agree It</text><text x="255" y="113.5">Visualize It</text><text x="307" y="113.5">Measure It</text>
      <text x="359" y="113.5">Improve It</text><text x="411" y="113.5">Recreate It</text><text x="462" y="113.5">Implement It</text>
    </g>
  </g>

  <g class="wastes">
    <rect x="10" y="158" width="22" height="90" rx="3" fill="#fff" stroke="var(--ink)" stroke-width="0.8"/>
    <text class="t-tiny mid t-bold" transform="translate(23 203) rotate(-90)">The 8 Wastes Lens</text>

    <g class="waste waste--defects">
      <circle cx="68" cy="168" r="11" fill="#fff" stroke="#e8452c"/><text class="mid t-bold" x="68" y="173" font-size="13" fill="#e8452c">D</text>
      <rect x="47" y="190" width="42" height="42" fill="#e8452c"/>
      <g class="icon-line" transform="translate(47 190)">
        <circle cx="21" cy="21" r="13"/><line x1="15" y1="15" x2="27" y2="27"/><line x1="27" y1="15" x2="15" y2="27"/>
      </g>
      <text class="t-tiny mid" x="68" y="242">Defects</text>
    </g>
    <g class="waste waste--overproduction">
      <circle cx="123" cy="168" r="11" fill="#fff" stroke="var(--purple)"/><text class="mid t-bold" x="123" y="173" font-size="13" fill="var(--purple)">O</text>
      <rect x="102" y="190" width="42" height="42" fill="var(--purple)"/>
      <g transform="translate(102 190)">
        <polygon class="icon-fill" points="8,32 8,18 16,22 16,18 24,22 24,18 32,22 32,10 36,10 36,32"/>
        <g fill="var(--purple)"><rect x="12" y="25" width="4" height="4"/><rect x="20" y="25" width="4" height="4"/><rect x="28" y="25" width="4" height="4"/></g>
      </g>
      <text class="t-tiny mid" x="123" y="242">Over Production</text>
    </g>
    <g class="waste waste--waiting">
      <circle cx="179" cy="168" r="11" fill="#fff" stroke="var(--red)"/><text class="mid t-bold" x="179" y="173" font-size="13" fill="var(--red)">W</text>
      <rect x="158" y="190" width="42" height="42" fill="var(--red)"/>
      <g transform="translate(158 190)">
        <rect class="icon-fill" x="11" y="7" width="20" height="3"/><rect class="icon-fill" x="11" y="32" width="20" height="3"/>
        <polygon class="icon-line" points="14,10 28,10 21,21 28,32 14,32 21,21"/>
        <polygon class="icon-fill" points="17,30 25,30 21,25"/>
      </g>
      <text class="t-tiny mid" x="179" y="242">Waiting</text>
    </g>
    <g class="waste waste--talent">
      <circle cx="238" cy="168" r="11" fill="#fff" stroke="var(--green)"/><text class="mid t-bold" x="238" y="173" font-size="13" fill="var(--green)">N</text>
      <rect x="217" y="190" width="42" height="42" fill="var(--green)"/>
      <g class="icon-fill" transform="translate(217 190)">
        <circle cx="12" cy="14" r="3"/><rect x="9" y="18" width="6" height="14" rx="2"/>
        <circle cx="21" cy="11" r="3.5"/><rect x="17.5" y="15.5" width="7" height="17" rx="2"/>
        <circle cx="30" cy="14" r="3"/><rect x="27" y="18" width="6" height="14" rx="2"/>
      </g>
      <text class="t-tiny mid" x="238" y="242">Non Utilized Talent</text>
    </g>
    <g class="waste waste--transport">
      <circle cx="296" cy="168" r="11" fill="#fff" stroke="var(--magenta)"/><text class="mid t-bold" x="296" y="173" font-size="13" fill="var(--magenta)">T</text>
      <rect x="275" y="190" width="42" height="42" fill="var(--magenta)"/>
      <g transform="translate(275 190)">
        <rect class="icon-fill" x="6" y="13" width="20" height="14"/>
        <polygon class="icon-fill" points="27,17 33,17 37,22 37,27 27,27"/>
        <g fill="#fff" stroke="var(--magenta)" stroke-width="1.5"><circle cx="12" cy="29" r="3.5"/><circle cx="31" cy="29" r="3.5"/></g>
      </g>
      <text class="t-tiny mid" x="296" y="242">Transportation</text>
    </g>
    <g class="waste waste--inventory">
      <circle cx="351" cy="168" r="11" fill="#fff" stroke="var(--yellow)"/><text class="mid t-bold" x="351" y="173" font-size="13" fill="var(--yellow)">I</text>
      <rect x="330" y="190" width="42" height="42" fill="var(--yellow)"/>
      <g transform="translate(330 190)">
        <polygon class="icon-fill" points="8,15 21,20 34,15 34,31 21,36 8,31"/>
        <polygon fill="none" stroke="#fff" stroke-width="1.6" stroke-linejoin="round" points="8,15 21,9 34,15 21,20"/>
        <line x1="21" y1="20" x2="21" y2="36" stroke="var(--yellow)" stroke-width="1.2"/>
      </g>
      <text class="t-tiny mid" x="351" y="242">Inventory</text>
    </g>
    <g class="waste waste--motion">
      <circle cx="407" cy="168" r="11" fill="#fff" stroke="#222"/><text class="mid t-bold" x="407" y="173" font-size="13" fill="#222">M</text>
      <rect x="386" y="190" width="42" height="42" fill="#222"/>
      <g class="icon-fill" transform="translate(386 190)">
        <polygon points="15,7 8,16 13,16 13,35 17,35 17,16 22,16"/>
        <polygon points="27,35 20,26 25,26 25,7 29,7 29,26 34,26"/>
      </g>
      <text class="t-tiny mid" x="407" y="242">Motion</text>
    </g>
    <g class="waste waste--processing">
      <circle cx="463" cy="168" r="11" fill="#fff" stroke="var(--purple)"/><text class="mid t-bold" x="463" y="173" font-size="13" fill="var(--purple)">E</text>
      <rect x="442" y="190" width="42" height="42" fill="var(--purple)"/>
      <g transform="translate(442 190)">
        <circle cx="16" cy="17" r="8" fill="none" stroke="#fff" stroke-width="4" stroke-dasharray="3 2.3"/>
        <circle cx="16" cy="17" r="5" fill="none" stroke="#fff" stroke-width="2"/>
        <circle cx="28" cy="28" r="6" fill="none" stroke="#fff" stroke-width="3.5" stroke-dasharray="2.5 2"/>
        <circle cx="28" cy="28" r="3.5" fill="none" stroke="#fff" stroke-width="1.6"/>
      </g>
      <text class="t-tiny mid" x="463" y="242">Extra Processing</text>
    </g>
  </g>

  <g class="method">
    <rect x="10" y="268" width="64" height="78" rx="4" fill="#fff" stroke="var(--purple)" stroke-width="0.8"/>
    <circle cx="42" cy="290" r="14" fill="var(--purple)" role="img" aria-label="Target icon"/>
    <text class="t-tiny mid" x="42" y="321">The <tspan fill="var(--red)">7 Step</tspan></text>
    <text class="t-tiny mid" x="42" y="328">Phoenix</text>
    <text class="t-tiny mid" x="42" y="335">Method</text>
    <line x1="82" y1="304" x2="490" y2="304" stroke="var(--ink)" stroke-width="0.6"/>
    <g fill="#fff" stroke-width="0.9">
      <rect x="103" y="310" width="14" height="12" stroke="var(--orange)"/>
      <rect x="154" y="290" width="14" height="12" stroke="var(--purple)"/>
      <rect x="204" y="310" width="14" height="12" stroke="var(--red)"/>
      <rect x="254" y="290" width="14" height="12" stroke="var(--green)"/>
      <rect x="304" y="310" width="14" height="12" stroke="var(--magenta)"/>
      <rect x="354" y="290" width="14" height="12" stroke="var(--yellow)"/>
      <rect x="404" y="310" width="14" height="12" stroke="var(--ink)"/>
    </g>
    <g font-size="8" text-anchor="middle">
      <text x="110" y="319" fill="var(--orange)">1</text><text x="161" y="299" fill="var(--purple)">2</text>
      <text x="211" y="319" fill="var(--red)">3</text><text x="261" y="299" fill="var(--green)">4</text>
      <text x="311" y="319" fill="var(--magenta)">5</text><text x="361" y="299" fill="var(--yellow)">6</text>
      <text x="411" y="319" fill="var(--ink)">7</text>
    </g>
    <g class="t-tiny" text-anchor="middle" font-size="5">
      <text x="110" y="282">Agree</text><text x="110" y="288">Measurable</text><text x="110" y="294">Business Value</text>
      <text x="161" y="314">Create</text><text x="161" y="320">A Product</text><text x="161" y="326">Backlog</text>
      <text x="211" y="282">Estimate What Is</text><text x="211" y="288">Possible With</text><text x="211" y="294">Deliverables</text>
      <text x="261" y="314">Prioritize</text><text x="261" y="320">Business</text><text x="261" y="326">Deliverables</text>
      <text x="311" y="288">Execute In</text><text x="311" y="294">Sprint Cycles</text>
      <text x="361" y="314">Make It</text><text x="361" y="320">Visable</text>
      <text x="411" y="288">Review</text><text x="411" y="294">Learn Adapt</text>
    </g>
    <rect x="446" y="294" width="32" height="16" rx="4" fill="var(--purple)"/>
    <text class="mid" x="462" y="301" font-size="5" fill="#fff">Repeat</text>
    <text class="mid" x="462" y="307" font-size="5" fill="#fff">£/$</text>
  </g>
</svg>
</section>

<!-- 60-Day Climb page -->
<section class="page page--climb">
<svg viewBox="0 0 496 352" aria-label="The 60-Day Climb">
  <rect x="0" y="0" width="496" height="352" fill="var(--gap)"/>
  <rect x="0" y="0" width="496" height="50" fill="#fff"/>
  <circle cx="36" cy="24" r="18" fill="var(--gap)" role="img" aria-label="60-Day Climb emblem"/>
  <text class="t-title" x="94" y="22" fill="var(--purple)">THE 60-DAY CLIMB</text>
  <rect x="72" y="28" width="424" height="16" fill="var(--purple)"/>
  <text class="t-band" x="94" y="40">An Execution System That Gets Your Team From <tspan font-weight="700" font-style="italic">HERE TO THERE</tspan> --- Faster</text>

  <!-- Column 1 -->
  <g class="column">
    <rect x="12" y="54" width="116" height="290" fill="#fff" stroke="var(--red)" stroke-width="0.8"/>
    <rect x="12" y="54" width="116" height="15" fill="var(--red)"/>
    <text class="mid t-bold" x="70" y="64" font-size="7" fill="#fff">Big Picture</text>
    <rect x="12" y="84" width="10" height="88" fill="var(--red)"/>
    <text class="mid" transform="translate(19 128) rotate(-90)" font-size="4.8" fill="#fff">4 Business Growth Pillars</text>
    <rect x="30" y="80" width="92" height="90" rx="4" fill="#fff" stroke="var(--red)" stroke-width="0.8"/>
    <g class="t-small">
      <text x="36" y="93">Leadership/Strategy</text>
      <text x="36" y="116">Sales/Marketing</text>
      <text x="36" y="138">Prodution/Fullfillment</text>
      <text x="36" y="161">Finance/Administration</text>
    </g>
    <g stroke="#999" stroke-width="0.5" stroke-dasharray="1 1.5">
      <line x1="36" y1="103" x2="118" y2="103"/><line x1="36" y1="126" x2="118" y2="126"/><line x1="36" y1="149" x2="118" y2="149"/>
    </g>
    <polygon points="26,176 114,176 114,184 70,194 26,184" fill="var(--red)"/>
    <text class="mid" x="70" y="186" font-size="10" fill="#fff">01</text>
    <text class="t-small mid" x="70" y="215"><tspan fill="var(--red)" font-weight="700">5-3-1</tspan> Vision</text>
    <polygon points="26,238 114,238 114,246 70,256 26,246" fill="var(--red)"/>
    <text class="mid" x="70" y="248" font-size="10" fill="#fff">02</text>
    <text class="t-small mid" x="70" y="275"><tspan fill="var(--red)" font-weight="700">1 Year</tspan> Action</text>
    <text class="t-small mid" x="70" y="284">Strategies</text>
    <rect x="12" y="302" width="116" height="42" fill="var(--red)"/>
    <text x="18" y="319" font-size="6.5" font-weight="700" fill="#fff">Creating Clarity</text>
    <text x="18" y="327" font-size="6.5" font-weight="700" fill="#fff">Of Outcome</text>
    <polygon points="84,314 128,314 128,342 72,342" fill="#fff"/>
    <text x="94" y="333" font-size="8" font-weight="700" fill="var(--ink)">Phase 1</text>
  </g>

  <!-- Column 2 -->
  <g class="column">
    <rect x="132" y="54" width="116" height="290" fill="#fff" stroke="var(--purple)" stroke-width="0.8"/>
    <rect x="132" y="54" width="116" height="15" fill="var(--purple)"/>
    <text class="mid t-bold" x="190" y="64" font-size="7" fill="#fff">The 4 Races</text>
    <g fill="var(--purple)">
      <polygon points="146,80 234,80 234,88 190,98 146,88"/>
      <polygon points="146,136 234,136 234,144 190,154 146,144"/>
      <polygon points="146,192 234,192 234,200 190,210 146,200"/>
      <polygon points="146,248 234,248 234,256 190,266 146,256"/>
    </g>
    <g font-size="10" fill="#fff" text-anchor="middle">
      <text x="190" y="90">03</text><text x="190" y="146">04</text><text x="190" y="202">05</text><text x="190" y="258">06</text>
    </g>
    <text class="t-small" x="145" y="111">The <tspan font-weight="700" fill="var(--purple)">4</tspan> Races</text>
    <text class="t-small" x="145" y="167">The <tspan font-weight="700" fill="var(--purple)">6</tspan> Sprints</text>
    <text class="t-small" x="145" y="223">The Sprint <tspan font-weight="700" fill="var(--purple)">Plan</tspan></text>
    <text class="t-small mid" x="190" y="279"><tspan font-weight="700" fill="var(--purple)" font-size="7.5">Daily</tspan> Stand Up Or</text>
    <text class="t-small mid" x="190" y="288">Buddy Call</text>
    <g fill="none" stroke="var(--purple)" stroke-width="1.2">
      <rect x="214" y="100" width="7" height="6"/><rect x="224" y="100" width="7" height="6"/>
      <rect x="214" y="109" width="7" height="6"/><rect x="224" y="109" width="7" height="6"/>
      <rect x="204" y="156" width="6" height="6"/><rect x="213" y="156" width="6" height="6"/><rect x="222" y="156" width="6" height="6"/>
      <rect x="204" y="165" width="6" height="6"/><rect x="213" y="165" width="6" height="6"/><rect x="222" y="165" width="6" height="6"/>
      <rect x="214" y="210" width="17" height="22" rx="1"/>
      <line x1="218" y1="216" x2="228" y2="216"/><line x1="218" y1="221" x2="228" y2="221"/><line x1="218" y1="226" x2="228" y2="226"/>
    </g>
    <rect x="132" y="302" width="116" height="42" fill="var(--purple)"/>
    <text x="138" y="319" font-size="6.5" font-weight="700" fill="#fff">Planning</text>
    <text x="138" y="327" font-size="6.5" font-weight="700" fill="#fff">The Path</text>
    <polygon points="204,314 248,314 248,342 192,342" fill="#fff"/>
    <text x="214" y="333" font-size="8" font-weight="700" fill="var(--ink)">Phase 2</text>
  </g>

  <!-- Column 3 -->
  <g class="column">
    <rect x="252" y="54" width="115" height="290" fill="#fff" stroke="var(--orange)" stroke-width="0.8"/>
    <rect x="252" y="54" width="115" height="15" fill="var(--orange)"/>
    <text class="mid t-bold" x="309" y="64" font-size="7" fill="#fff">Sprint Review</text>
    <g fill="var(--orange)">
      <polygon points="265,80 353,80 353,88 309,98 265,88"/>
      <polygon points="265,138 353,138 353,146 309,156 265,146"/>
      <polygon points="265,196 353,196 353,204 309,214 265,204"/>
    </g>
    <g font-size="10" fill="#fff" text-anchor="middle">
      <text x="309" y="90">07</text><text x="309" y="148">08</text><text x="309" y="206">09</text>
    </g>
    <text class="t-small mid" x="309" y="111">Execution <tspan font-weight="700" fill="var(--orange)">Score</tspan></text>
    <text class="t-small mid" x="309" y="119"># ?</text>
    <text class="t-small" x="264" y="168" font-size="7.5"><tspan font-weight="700" fill="var(--orange)">Learn</tspan> And <tspan font-weight="700" fill="var(--orange)">Adapt</tspan></text>
    <rect x="336" y="157" width="16" height="13" fill="none" stroke="var(--orange)"/>
    <line x1="344" y1="157" x2="344" y2="170" stroke="var(--orange)" stroke-width="0.8"/>
    <text class="t-small mid" x="309" y="226">Action <tspan font-weight="700" fill="var(--orange)">Velocity</tspan> Step</text>
    <rect x="285" y="232" width="48" height="12" fill="var(--orange)"/>
    <text class="mid t-bold" x="309" y="241" font-size="7" fill="#fff">1 Action</text>
    <rect x="252" y="302" width="115" height="42" fill="var(--orange)"/>
    <text x="258" y="323" font-size="6.5" font-weight="700" fill="#fff">Learn &amp; Grow</text>
    <polygon points="323,314 367,314 367,342 311,342" fill="#fff"/>
    <text x="333" y="333" font-size="8" font-weight="700" fill="var(--ink)">Phase 3</text>
  </g>

  <!-- Column 4 -->
  <g class="column">
    <rect x="372" y="54" width="115" height="290" fill="#fff" stroke="var(--green)" stroke-width="0.8"/>
    <rect x="372" y="54" width="115" height="15" fill="var(--green)"/>
    <text class="mid t-bold" x="429" y="64" font-size="7" fill="#fff">Up Level</text>
    <g fill="var(--green)">
      <polygon points="385,80 473,80 473,88 429,98 385,88"/>
      <polygon points="385,136 473,136 473,144 429,154 385,144"/>
      <polygon points="385,192 473,192 473,200 429,210 385,200"/>
      <polygon points="385,248 473,248 473,256 429,266 385,256"/>
    </g>
    <g font-size="10" fill="#fff" text-anchor="middle">
      <text x="429" y="90">10</text><text x="429" y="146">11</text><text x="429" y="202">12</text><text x="429" y="258">13</text>
    </g>
    <text class="t-small" x="384" y="111"><tspan font-weight="700" fill="var(--green)">Race</tspan> Review</text>
    <text class="t-small" x="384" y="165">Review Steps <tspan font-weight="700" fill="var(--green)">1-3</tspan></text>
    <rect x="448" y="160" width="30" height="7" fill="var(--green)"/>
    <text x="451" y="165.5" font-size="4.5" fill="#fff">Update</text>
    <text class="t-small" x="384" y="221">The <tspan font-weight="700" fill="var(--green)">6</tspan> Sprints</text>
    <text class="t-small" x="384" y="279">New Sprint <tspan font-weight="700" fill="var(--green)">Plan</tspan></text>
    <g fill="none" stroke="var(--green)" stroke-width="1.2">
      <rect x="449" y="98" width="24" height="16"/>
      <polyline points="452,111 458,104 463,108 470,101"/>
      <rect x="444" y="206" width="6" height="6"/><rect x="454" y="206" width="6" height="6"/><rect x="464" y="206" width="6" height="6"/>
      <rect x="444" y="216" width="6" height="6"/><rect x="454" y="216" width="6" height="6"/><rect x="464" y="216" width="6" height="6"/>
      <rect x="454" y="262" width="17" height="22" rx="1"/>
      <line x1="458" y1="268" x2="468" y2="268"/><line x1="458" y1="273" x2="468" y2="273"/><line x1="458" y1="278" x2="468" y2="278"/>
    </g>
    <rect x="372" y="302" width="115" height="42" fill="var(--green)"/>
    <text x="378" y="319" font-size="6.5" font-weight="700" fill="#fff">Repeat &amp;</text>
    <text x="378" y="327" font-size="6.5" font-weight="700" fill="#fff">Accelerate</text>
    <polygon points="443,314 487,314 487,342 431,342" fill="#fff"/>
    <text x="453" y="333" font-size="8" font-weight="700" fill="var(--ink)">Phase 4</text>
  </g>
</svg>
</section>

<!-- Lean Leadership page -->
<section class="page page--lean">
<svg viewBox="0 0 496 352" aria-label="Lean Leadership">
  <defs>
    <path id="talentTop" d="M26,140 A60,60 0 0,1 146,140"/>
    <path id="talentBottom" d="M20,140 A66,66 0 0,0 152,140"/>
    <path id="pipelineTop" d="M350,140 A60,60 0 0,1 470,140"/>
    <path id="pipelineBottom" d="M342,140 A68,68 0 0,0 478,140"/>
  </defs>
  <rect x="0" y="44" width="496" height="308" fill="#fff"/>
  <rect x="164" y="44" width="4" height="308" fill="var(--gap)"/>
  <rect x="324" y="44" width="6" height="308" fill="var(--gap)"/>
  <rect x="8" y="6" width="20" height="20" fill="var(--gap)" role="img" aria-label="Lean Leadership emblem"/>
  <text class="t-title" x="46" y="22" fill="var(--purple)">LEAN LEADERSHIP</text>
  <rect x="42" y="28" width="454" height="16" fill="var(--purple)"/>
  <text class="t-band mid" x="269" y="40">A Commonsense Approach To Building And Leading A Team That Delivers Exceptional Results</text>

  <g class="talent-cycle">
    <circle cx="86" cy="140" r="63" fill="none" stroke="var(--green)" stroke-width="12"/>
    <circle cx="86" cy="140" r="48" fill="#fff" stroke="var(--green)" stroke-width="3"/>
    <g font-size="9" fill="#fff">
      <text><textPath href="#talentTop" startOffset="40%" text-anchor="middle">Find</textPath></text>
      <text><textPath href="#talentBottom" startOffset="62%" text-anchor="middle">Train</textPath></text>
    </g>
    <text transform="translate(89 140) rotate(-90) translate(-22 -59)" font-size="9" fill="#fff">Retain</text>
    <text transform="translate(83 140) rotate(90) translate(-22 -59)" font-size="9" fill="#fff">Hire</text>
    <g font-size="8.5" font-weight="700" fill="var(--ink)" text-anchor="middle">
      <text x="86" y="126">Talent Analysis</text><text x="86" y="137">A/B/C</text>
      <text x="86" y="148">Culture</text><text x="86" y="159">Performance Pay</text>
    </g>
  </g>

  <g class="business-plan">
    <rect x="196" y="78" width="16" height="162" rx="8" fill="var(--orange)"/>
    <text class="mid t-bold" transform="translate(207 159) rotate(-90)" font-size="8" fill="#fff">M 7 Business Plan</text>
    <rect x="218" y="78" width="82" height="162" rx="4" fill="#fff" stroke="var(--orange)" stroke-width="0.8"/>
    <g font-size="9" fill="var(--ink)">
      <text x="229" y="93">Market</text><text x="229" y="116">Message</text><text x="229" y="139">Members</text>
      <text x="229" y="162">Manage</text><text x="229" y="185">Money</text><text x="229" y="208">Metrics</text><text x="229" y="231">Mission</text>
    </g>
    <g stroke="#999" stroke-width="0.5" stroke-dasharray="1 1.5">
      <line x1="224" y1="101" x2="296" y2="101"/><line x1="224" y1="124" x2="296" y2="124"/><line x1="224" y1="147" x2="296" y2="147"/>
      <line x1="224" y1="170" x2="296" y2="170"/><line x1="224" y1="193" x2="296" y2="193"/><line x1="224" y1="216" x2="296" y2="216"/>
    </g>
  </g>

  <g class="pipeline">
    <circle cx="410" cy="140" r="64" fill="none" stroke="var(--purple)" stroke-width="15"/>
    <g font-size="9" fill="#fff" text-anchor="middle">
      <text><textPath href="#pipelineTop" startOffset="30%">Time To Close</textPath></text>
      <text><textPath href="#pipelineTop" startOffset="80%">Quantity</textPath></text>
      <text><textPath href="#pipelineBottom" startOffset="25%">Conversion%</textPath></text>
      <text><textPath href="#pipelineBottom" startOffset="78%">Quality</textPath></text>
    </g>
    <rect x="369" y="124" width="82" height="32" rx="6" fill="var(--purple)"/>
    <text class="mid t-bold" x="410" y="138" font-size="9" fill="#fff">Pipeline</text>
    <text class="mid t-bold" x="410" y="150" font-size="9" fill="#fff">Acceleration</text>

    <rect x="336" y="234" width="46" height="42" rx="3" fill="#fff" stroke="var(--purple)"/>
    <rect x="336" y="234" width="46" height="9" fill="var(--purple)"/>
    <text class="mid" x="359" y="241" font-size="5.5" fill="#fff">Hot List</text>
    <text class="mid" x="359" y="256" font-size="6" fill="var(--ink)">New</text>
    <line x1="341" y1="260" x2="377" y2="260" stroke="#999" stroke-width="0.5" stroke-dasharray="1 1.5"/>
    <text class="mid" x="359" y="268" font-size="6" fill="var(--ink)">Upgrades</text>

    <rect x="386" y="234" width="94" height="42" rx="3" fill="#fff" stroke="var(--purple)"/>
    <rect x="386" y="234" width="94" height="9" fill="var(--purple)"/>
    <text class="mid" x="433" y="241" font-size="5.5" fill="#fff">Funnel On The Wall</text>
    <g fill="none" stroke="var(--purple)" stroke-width="0.8">
      <rect x="390" y="246" width="28" height="26"/><rect x="420" y="246" width="28" height="26"/><rect x="450" y="246" width="27" height="26"/>
    </g>
    <g font-size="4.5" fill="var(--ink)">
      <text transform="translate(397 269) rotate(-90)">Interested</text>
      <text transform="translate(427 269) rotate(-90)">Engaged</text>
      <text transform="translate(457 269) rotate(-90)">Buying</text>
    </g>
  </g>

  <rect x="10" y="310" width="154" height="25" fill="var(--green)"/>
  <text class="mid t-bold" x="87" y="326" font-size="10" fill="#fff">A-Player Blueprint</text>
  <rect x="170" y="310" width="154" height="25" fill="var(--orange)"/>
  <text class="mid t-bold" x="247" y="326" font-size="10" fill="#fff">M7 Business Plan</text>
  <rect x="332" y="310" width="154" height="25" fill="var(--purple)"/>
  <text class="mid t-bold" x="409" y="326" font-size="10" fill="#fff">Sales Acceleration</text>
</svg>
</section>

</body>
</html>
```